IT Company Business Card design

Brisk Node is a new computer solutions business focusing on setting up servers and computer systems for small to medium sized businesses.

A business client will either request a solution, or support for a current system and we will turn up on site to provide these services.

We are bast in Christchurch, New Zealand.

We are looking for unique business card's that stand out and show off the business in a professional light.

Open to all idea's etc.

Industry/Entity Type

Computer

Requirements
Must have
• Business Logo (AI file attached)
Employee Name
Business title
Business landline number
Cell phone number
Email
Web URL
Nice to have
• Could be nice to have some keywords (possibly on the back) such as:

Business IT solutions
Network installations
Phone solutions
Server management
Software diagnostics

The above is not needed, just an idea.

```html
<!DOCTYPE html>
<html lang="en">
<head>
<meta charset="utf-8">
<title>Brisk Node – Business Card</title>
<link rel="stylesheet" href="https://fonts.googleapis.com/css2?family=Jost:wght@400;500&display=swap">
<style>
  :root {
    --paper: #ffffff;
    --paper-shade: #ececec;
    --ink: #1a1a1a;
    --ink-soft: #444444;
    --night: #060606;
    --night-facet: #161616;
    --steel-light: #a8a8a8;
    --steel-dark: #3a3a3a;
    --brand-blue: #1a3fd0;
    --brand-deep: #0a1f8f;
    --brand-cyan: #29e4f4;
    --brand-mint: #6fdcb0;
    --white: #ffffff;
  }
  * { margin: 0; padding: 0; box-sizing: border-box; }
  html, body { width: 1200px; height: 880px; overflow: hidden; background: var(--paper); }
  body { font-family: "Jost", "Helvetica Neue", Arial, sans-serif; }
  .canvas { position: relative; width: 1200px; height: 880px; overflow: hidden; }
  .backdrop { position: absolute; inset: 0; }

  .brand-mark {
    position: absolute;
    border-radius: 50%;
    background: linear-gradient(135deg, var(--brand-cyan), var(--brand-blue) 60%, var(--brand-deep));
  }
  .brand-divider { position: absolute; width: 2px; }
  .brand-name { position: absolute; font-weight: 400; white-space: nowrap; }

  /* Front face */
  .front .brand-mark { left: 69px; top: 169px; width: 172px; height: 172px; }
  .front .brand-divider { left: 268px; top: 174px; height: 174px; background: var(--ink-soft); }
  .front .brand-name { left: 292px; top: 206px; font-size: 62px; letter-spacing: 3px; color: var(--ink); line-height: 1; }
  .front .web-url { position: absolute; left: 300px; top: 281px; font-size: 21px; letter-spacing: 3.2px; color: var(--ink); }

  /* Back face */
  .back .brand-mark { left: 101px; top: 629px; width: 72px; height: 72px; }
  .back .brand-divider { left: 188px; top: 640px; height: 56px; background: var(--white); width: 1.5px; }
  .back .brand-name { left: 198px; top: 656px; font-size: 24px; letter-spacing: 2px; color: var(--white); line-height: 1; }
  .person-name { position: absolute; left: 104px; top: 727px; font-size: 31px; font-variant: small-caps; letter-spacing: 2px; color: var(--white); }
  .person-email { position: absolute; left: 104px; top: 767px; font-size: 14.5px; letter-spacing: 1.2px; color: var(--white); }
  .feature-disc { position: absolute; left: 770px; top: 462px; width: 388px; height: 388px; }
</style>
</head>
<body>
<main class="canvas">
  <svg class="backdrop" width="1200" height="880" viewBox="0 0 1200 880" aria-hidden="true">
    <defs>
      <linearGradient id="band-glow" x1="0" y1="0" x2="1" y2="0">
        <stop offset="0" stop-color="#1a3fd0"/>
        <stop offset="0.22" stop-color="#1f55e8"/>
        <stop offset="0.4" stop-color="#4fb6f2"/>
        <stop offset="0.52" stop-color="#6fdcb0"/>
        <stop offset="0.66" stop-color="#3aa8f0"/>
        <stop offset="0.8" stop-color="#1a3fd0"/>
        <stop offset="1" stop-color="#1a3fd0"/>
      </linearGradient>
      <linearGradient id="steel" x1="0" y1="0" x2="1" y2="1">
        <stop offset="0" stop-color="#2e2e2e"/>
        <stop offset="1" stop-color="#b0b0b0"/>
      </linearGradient>
      <linearGradient id="paper-facet" x1="0" y1="0" x2="1" y2="1">
        <stop offset="0" stop-color="#e6e6e6"/>
        <stop offset="1" stop-color="#ffffff"/>
      </linearGradient>
    </defs>
    <!-- front face facets -->
    <rect width="1200" height="520" fill="#ffffff"/>
    <polygon points="305,0 1200,0 1200,420 560,510" fill="url(#paper-facet)" opacity="0.7"/>
    <polygon points="950,0 1200,0 1200,330" fill="#f2f2f2"/>
    <polygon points="0,0 305,0 90,510 0,510" fill="#f7f7f7"/>
    <polygon points="450,250 1200,520 560,520" fill="#eeeeee"/>
    <!-- back face -->
    <rect y="509" width="1200" height="371" fill="var(--night)"/>
    <polygon points="160,556 430,556 300,880 60,880" fill="#0e0e0e"/>
    <polygon points="430,556 720,556 640,880 300,880" fill="#0a0a0a"/>
    <polygon points="1080,556 1200,556 1200,880 740,880" fill="url(#steel)"/>
    <rect y="509" width="1200" height="47" fill="url(#band-glow)"/>
  </svg>

  <section class="front" aria-label="Card front">
    <span class="brand-mark" aria-hidden="true"></span>
    <span class="brand-divider" aria-hidden="true"></span>
    <h1 class="brand-name">BRISK NODE</h1>
    <p class="web-url">WWW.BRISKNODE.CO.NZ</p>
  </section>

  <section class="back" aria-label="Card back">
    <span class="brand-mark" aria-hidden="true"></span>
    <span class="brand-divider" aria-hidden="true"></span>
    <p class="brand-name">BRISK NODE</p>
    <p class="person-name">Liam Hartley</p>
    <p class="person-email">INFO@BRISKNODE.CO.NZ</p>
    <svg class="feature-disc" viewBox="0 0 388 388" aria-hidden="true">
      <circle cx="194" cy="194" r="186" fill="none" stroke="var(--brand-blue)" stroke-width="14"/>
    </svg>
  </section>
</main>
</body>
</html>
```